Velmora - 3D medical animations and high end visual content

Our company creates high end visual content and animations for medical global companies.
Our website - www.velmora-studio.example
We would like to have an amazing business card for our CEO that he can use in the following exhebitions he is going to attend.
It is very important that the design will be memorable and diffrent. It has to reflect our brand design (you can have it from our website)
We would like to transmit innovation, prestige, luxury, aesthetics.
The card has to be Double Sided

Target Market(s)

Marketing managers in medical global companys

Industry/Entity Type

It Company

Contact Information for Business Card

Requirements
Nice to have
• It is very important that the design will be memorable and diffrent. It has to reflect our brand design (you can have it from our website)

```html
<!DOCTYPE html>
<html lang="en">
<head>
<meta charset="utf-8">
<title>Velmora – Business Card</title>
<link rel="stylesheet" href="https://fonts.googleapis.com/css2?family=Open+Sans:wght@400;600;700&display=swap">
<style>
  :root {
    --bg: #e6e7e9;
    --teal: #2e9bb3;
    --teal-dark: #27879c;
    --ink: #1b1b1b;
    --paper: #ffffff;
    --logo-ink: #2b2b2b;
    --muted: #e8e8e8;
  }
  * { box-sizing: border-box; margin: 0; padding: 0; }
  html, body {
    width: 1200px; height: 977px; overflow: hidden;
    background: var(--bg);
    font-family: "Open Sans", Arial, sans-serif;
  }
  .canvas {
    position: relative; width: 1200px; height: 977px;
  }
  .card {
    position: absolute; left: 250px; width: 700px; height: 400px;
    overflow: hidden;
    box-shadow: 0 6px 18px rgba(0,0,0,0.18);
  }
  .card--front { top: 70px; background: var(--teal); }
  .card--back { top: 507px; background: var(--paper); }

  .brand-name {
    position: absolute;
    font-weight: 600;
    letter-spacing: 6px;
    text-transform: uppercase;
    white-space: nowrap;
  }
  .card--front .brand-name {
    left: 0; right: 0; top: 168px; text-align: center;
    font-size: 52px; color: var(--paper);
  }
  .card--back .brand-name {
    left: 490px; top: 177px; font-size: 30px; letter-spacing: 4px;
    color: var(--logo-ink);
  }

  .back-shapes { position: absolute; inset: 0; }

  .contact {
    position: absolute; left: 60px; top: 140px; color: var(--paper);
  }
  .contact__name { font-size: 24px; font-weight: 600; letter-spacing: 0.5px; }
  .contact__role { font-size: 13px; font-weight: 600; margin-top: 4px; margin-left: 6px; }
  .contact__list { list-style: none; margin-top: 26px; margin-left: 14px; }
  .contact__item {
    display: flex; align-items: center; gap: 12px;
    font-size: 14px; color: var(--muted); height: 24px;
  }
  .contact__icon { width: 14px; height: 14px; flex: none; }
</style>
</head>
<body>
<main class="canvas">

  <section class="card card--front" aria-label="Card front">
    <div class="brand-name">Velmora</div>
  </section>

  <section class="card card--back" aria-label="Card back">
    <svg class="back-shapes" width="700" height="400" viewBox="0 0 700 400" aria-hidden="true">
      <polygon points="0,0 370,0 470,400 0,400" fill="var(--ink)"/>
      <polygon points="375,0 412,0 478,400 470,400" fill="var(--teal)"/>
    </svg>

    <div class="contact">
      <h1 class="contact__name">Eitan Marlow</h1>
      <p class="contact__role">Founder &amp; CEO</p>
      <ul class="contact__list">
        <li class="contact__item">
          <svg class="contact__icon" viewBox="0 0 14 14"><rect x="3.5" y="0.5" width="7" height="13" rx="1.5" fill="none" stroke="currentColor" stroke-width="1.3"/><circle cx="7" cy="11" r="0.9" fill="currentColor"/></svg>
          +972-52-5550142
        </li>
        <li class="contact__item">
          <svg class="contact__icon" viewBox="0 0 14 14"><polygon points="7,1 13,7 11,7 11,13 3,13 3,7 1,7" fill="currentColor"/></svg>
          +972-77-5550187
        </li>
        <li class="contact__item">
          <svg class="contact__icon" viewBox="0 0 14 14"><rect x="0.5" y="2.5" width="13" height="9" fill="currentColor"/><polyline points="0.5,2.5 7,8 13.5,2.5" fill="none" stroke="var(--ink)" stroke-width="1.2"/></svg>
          eitan@velmora-studio.example
        </li>
        <li class="contact__item">
          <svg class="contact__icon" viewBox="0 0 14 14"><circle cx="7" cy="7" r="6" fill="none" stroke="currentColor" stroke-width="1.3"/><ellipse cx="7" cy="7" rx="2.6" ry="6" fill="none" stroke="currentColor" stroke-width="1"/><line x1="1" y1="7" x2="13" y2="7" stroke="currentColor" stroke-width="1"/></svg>
          www.velmora-studio.example
        </li>
      </ul>
    </div>

    <div class="brand-name">Velmora</div>
  </section>

</main>
</body>
</html>
```